Fern Lantern Cannabis Cartridge box

Box with both inside and outside box. A disposable cannabis vape cart is the contents of the package. initial thoughts were black exterior box with color highlight. (example of 7 mint attached). There are four colors currently being used for the actual product. Black, White, Green and Blue. product will sit in retail display box. It should both "pop" and still emote quality and class.

Target Market(s)

Professional, discreet cannabis consumer. Experienced and knowledgeable

Industry/Entity Type

Cannabis

Font styles to use
Serif

Colors

Designer to choose colors to be used in the design.

Requirements
Must have
• use logo and logo colors
Nice to have
• elegant look. metalic foil printing, embossing available

```html
<!DOCTYPE html>
<html lang="en">
<head>
<meta charset="UTF-8">
<title>Fern Lantern – CBD Disposable Pod Device Boxes</title>
<link href="https://fonts.googleapis.com/css2?family=Montserrat:wght@400;500;700&display=swap" rel="stylesheet">
<style>
  :root {
    --backdrop: #c5c2c3;
    --box-black: #000000;
    --box-edge: #3b3a3b;
    --ink-white: #ffffff;
    --ink-black: #000000;
    --brand-teal: #1fae8c;
    --accent-green: #1fae8c;
    --accent-blue: #2a8ad0;
    --accent-white: #ffffff;
    --accent-grey: #8d8c8e;
  }
  * { box-sizing: border-box; margin: 0; padding: 0; }
  html, body {
    width: 1200px;
    height: 748px;
    overflow: hidden;
    background: var(--backdrop);
    font-family: "Montserrat", Arial, sans-serif;
  }
  .lineup {
    position: relative;
    width: 1200px;
    height: 748px;
  }
  .box-front {
    position: absolute;
    top: 117px;
    width: 184px;
    height: 519px;
    background: var(--box-black);
    border: 4px solid var(--box-edge);
    overflow: hidden;
    box-shadow: 4px 6px 8px rgba(0,0,0,0.18);
  }
  .box-front--green { left: 110px; --accent: var(--accent-green); }
  .box-front--blue  { left: 375px; --accent: var(--accent-blue); }
  .box-front--white { left: 640px; --accent: var(--accent-white); }
  .box-front--grey  { left: 904px; --accent: var(--accent-grey); }

  .brand-name {
    position: absolute;
    top: 96px;
    left: 0;
    right: 0;
    text-align: center;
    color: var(--brand-teal);
    font-weight: 700;
    font-size: 24px;
    line-height: 1.05;
    letter-spacing: 2px;
  }
  .colour-wash {
    position: absolute;
    left: 0;
    right: 0;
    bottom: 0;
    height: 236px;
    background: linear-gradient(to bottom, rgba(0,0,0,0) 0%, var(--accent) 100%);
    opacity: 0.95;
  }
  .product-type {
    position: absolute;
    top: 205px;
    left: 22px;
    color: var(--ink-white);
  }
  .product-type__cbd {
    display: block;
    font-weight: 700;
    font-size: 28px;
    line-height: 32px;
    letter-spacing: 0.5px;
  }
  .product-type__desc {
    display: block;
    font-weight: 400;
    font-size: 20px;
    line-height: 24px;
    letter-spacing: 0.4px;
  }
  .volume {
    position: absolute;
    left: 22px;
    bottom: 18px;
    color: var(--ink-white);
    font-weight: 700;
    font-size: 16px;
  }
  .box-front--white .volume { color: var(--ink-black); }
</style>
</head>
<body>
<main class="lineup">
  <section class="box-front box-front--green">
    <div class="brand-name">FERN<br>LANTERN</div>
    <div class="colour-wash" role="img" aria-label="Green halftone dot fade rising from the bottom"></div>
    <h2 class="product-type">
      <span class="product-type__cbd">CBD</span>
      <span class="product-type__desc">DISPOSABLE<br>POD DEVICE</span>
    </h2>
    <p class="volume">1.0ML</p>
  </section>

  <section class="box-front box-front--blue">
    <div class="brand-name">FERN<br>LANTERN</div>
    <div class="colour-wash" role="img" aria-label="Blue halftone dot fade rising from the bottom"></div>
    <h2 class="product-type">
      <span class="product-type__cbd">CBD</span>
      <span class="product-type__desc">DISPOSABLE<br>POD DEVICE</span>
    </h2>
    <p class="volume">1.0ML</p>
  </section>

  <section class="box-front box-front--white">
    <div class="brand-name">FERN<br>LANTERN</div>
    <div class="colour-wash" role="img" aria-label="White halftone dot fade rising from the bottom"></div>
    <h2 class="product-type">
      <span class="product-type__cbd">CBD</span>
      <span class="product-type__desc">DISPOSABLE<br>POD DEVICE</span>
    </h2>
    <p class="volume">1.0ML</p>
  </section>

  <section class="box-front box-front--grey">
    <div class="brand-name">FERN<br>LANTERN</div>
    <div class="colour-wash" role="img" aria-label="Grey halftone dot fade rising from the bottom"></div>
    <h2 class="product-type">
      <span class="product-type__cbd">CBD</span>
      <span class="product-type__desc">DISPOSABLE<br>POD DEVICE</span>
    </h2>
    <p class="volume">1.0ML</p>
  </section>
</main>
</body>
</html>
```